Awesome Digital Ad Design – Pellucid Adreach

I am going to be setting up a Pellucid Adreach ad campaign I need creatives for.

Several sizes are needed in the end, however, please submit your design concept in the following 2 sizes to start:
Medium rectangle: 300X250
Leaderboard: 728X90

Original artwork/design files and images used expected upon payment and as part of the final delivery.

Ads should match our company brand and the information on this webpage: http://www.harborlyneworks.com/real-estate-marketing/
SEE MORE INSTRUCTIONS IN ATTACHED WORD DOC
Updates

Target Market(s)

Business-To-Business Audience –Real Estate Company Executives (Presidents/VPs/Owners/CEOs/Sales Managers).

Industry/Entity Type

Real Estate

Font styles to use
Sans Serif

Requirements
Must have
• Copy should be minimal words, billboard like. Please use real photos/images that would appeal to real estate high-level decision-maker executives.
Should not have
• No cartoons or graphics

```html
<!DOCTYPE html>
<html lang="en">
<head>
<meta charset="utf-8">
<title>Harborlyne Works – Pellucid Adreach Banners</title>
<link rel="stylesheet" href="https://fonts.googleapis.com/css2?family=Oswald:wght@500;600&family=Open+Sans:wght@400;700&display=swap">
<style>
  :root {
    --canvas: #dedad7;
    --ad-bg: #ffffff;
    --ad-border: #2b2b2b;
    --headline: #6b2840;
    --subline: #111111;
    --cta: #f26722;
    --cta-text: #ffffff;
    --divider: #4a6a8e;
    --brand: #5c6670;
    --photo-light: #f4f5f6;
    --photo-mid: #8a8c92;
    --photo-dark: #3a3b40;
  }
  * { margin: 0; padding: 0; box-sizing: border-box; }
  html, body {
    width: 1200px; height: 900px; overflow: hidden;
    background: var(--canvas);
  }
  .stage { position: relative; width: 1200px; height: 900px; }

  .ad {
    position: absolute;
    background: var(--ad-bg);
    border: 1.5px solid var(--ad-border);
    overflow: hidden;
  }

  .brand-name {
    position: absolute;
    font-family: "Open Sans", sans-serif;
    font-weight: 400;
    color: var(--brand);
    line-height: 1.15;
  }

  .photo {
    position: absolute;
    background: linear-gradient(90deg, var(--photo-light) 0%, var(--photo-mid) 35%, var(--photo-dark) 60%, var(--photo-mid) 82%, var(--photo-light) 100%);
  }
  .photo::after {
    content: "";
    position: absolute; left: 0; right: 0; bottom: 0; height: 30%;
    background: linear-gradient(180deg, rgba(255,255,255,0) 0%, rgba(240,240,242,0.85) 100%);
  }

  .divider { position: absolute; background: var(--divider); }

  .headline {
    font-family: "Oswald", sans-serif;
    font-weight: 600;
    color: var(--headline);
    font-size: 32px;
    line-height: 36px;
    letter-spacing: 0.3px;
    white-space: nowrap;
  }
  .subline {
    font-family: "Oswald", sans-serif;
    font-weight: 500;
    color: var(--subline);
    font-size: 27px;
    line-height: 32px;
    white-space: nowrap;
  }
  .cta {
    display: inline-flex; align-items: center; justify-content: center;
    width: 212px; height: 54px;
    background: var(--cta);
    color: var(--cta-text);
    border-radius: 3px;
    font-family: "Open Sans", sans-serif;
    font-weight: 700;
    font-size: 27px;
    letter-spacing: 0.3px;
    text-decoration: none;
  }
  .copy {
    position: absolute;
    display: flex; flex-direction: column; align-items: center;
    text-align: center;
  }

  /* Leaderboard 728x90 */
  .leaderboard { left: 54px; top: 163px; width: 1092px; height: 135px; }
  .leaderboard .brand-name { left: 14px; top: 44px; font-size: 15px; }
  .leaderboard .photo { left: 132px; top: 0; width: 406px; height: 100%; }
  .leaderboard .divider { left: 538px; top: 0; width: 6px; height: 100%; }
  .leaderboard .copy { left: 544px; right: 0; top: 4px; }
  .leaderboard .cta { margin-top: 5px; }

  /* Medium rectangle 300x250 */
  .rectangle { left: 390px; top: 396px; width: 450px; height: 375px; }
  .rectangle .photo { left: 0; top: 0; width: 100%; height: 201px; }
  .rectangle .brand-name { left: 10px; top: 36px; font-size: 15px; z-index: 1; }
  .rectangle .divider { left: 0; top: 201px; width: 100%; height: 6px; }
  .rectangle .copy { left: 0; right: 0; top: 218px; }
  .rectangle .cta { margin-top: 22px; }
</style>
</head>
<body>
<main class="stage">

  <section class="ad leaderboard" aria-label="Leaderboard banner 728 by 90">
    <div class="brand-name">Harborlyne<br>Works</div>
    <div class="photo" role="img" aria-label="Photo of a businessman in a suit signing papers beside a small model house"></div>
    <div class="divider"></div>
    <div class="copy">
      <h2 class="headline">CLIENT FOLLOW-UP MADE SIMPLE</h2>
      <p class="subline">VIRTUALLY NO COST TO YOUR COMPANY!</p>
      <a class="cta" href="http://www.harborlyneworks.com/real-estate-marketing/">LEARN MORE</a>
    </div>
  </section>

  <section class="ad rectangle" aria-label="Medium rectangle banner 300 by 250">
    <div class="photo" role="img" aria-label="Photo of a businessman in a suit signing papers beside a small model house"></div>
    <div class="brand-name">Harborlyne<br>Works</div>
    <div class="divider"></div>
    <div class="copy">
      <h2 class="headline">CLIENT FOLLOW-UP MADE SIMPLE</h2>
      <p class="subline">VIRTUALLY NO COST TO YOUR COMPANY!</p>
      <a class="cta" href="http://www.harborlyneworks.com/real-estate-marketing/">LEARN MORE</a>
    </div>
  </section>

</main>
</body>
</html>
```